Larkmoor Forum Flyer to describe services

I provide data abstraction and consulting services to hospitals that are participating in an accreditation program for their bariatric surgery program. I need a flyer that I can hand out to potential clients that describes the services that I offer. I am attaching an info sheet that has the information on the services I offer. (One exception is that I no longer offer the remote dietitian services listed on the flyer) . I am also including a file with my logo. I would like this flyer to hand out at conferences where I meet people that might not be familiar with my business or who are not knowledgeable of how my services might benefit them. The most important service that I offer is the data abstraction subcontracting. I will provide a PPT that will provide further info on this service.

Target Market(s)

Bariatric program directors and surgeons

Industry/Entity Type

Healthcare

Font styles to use
Serif
Sans Serif

Colors

Designer to choose colors to be used in the design.

Requirements
Must have
• a description of the services I offer
• how subcontracting will benefit them and save them money
• something noting my experience as I am one of the most experienced professionals in this field of bariatric surgery accreditation
Nice to have
• I am not a designer and created the flyer that I have provided. I realize it is not very professional and would like something that looks fresh and professional.
Should not have
• I don't want it to be too wordy and yet it needs to have a description of services offered. I want to include the yellow in my logo, but the flyer sample I have given you has waaaaay too much yellow and want to tone that down!

```html
<!DOCTYPE html>
<html lang="en">
<head>
<meta charset="utf-8">
<title>Hollis Varga Consulting – Services Flyer</title>
<link href="https://fonts.googleapis.com/css2?family=Montserrat:ital,wght@0,300;0,400;0,500;0,600;0,700;0,800;1,500;1,600;1,700&display=swap" rel="stylesheet">
<style>
  :root{
    --yellow:#f7d417;
    --ink:#1d1d1b;
    --white:#ffffff;
    --page:#ffffff;
    --photo-a:#f4f2ef;
    --photo-b:#d9c6b3;
    --photo-c:#2f55a8;
  }
  *{box-sizing:border-box;margin:0;padding:0}
  html,body{width:1200px;height:1000px;overflow:hidden;background:var(--page)}
  body{font-family:'Montserrat',sans-serif;color:var(--ink);position:relative}
  .flyer{position:absolute;left:14px;top:42px;width:1174px;height:906px;background:var(--white);box-shadow:0 0 6px rgba(0,0,0,.25);overflow:hidden}
  .side-panel{position:absolute;left:0;top:0;width:483px;height:906px;background:var(--white)}
  .main-panel{position:absolute;left:483px;top:0;width:691px;height:906px;background:var(--yellow)}

  .brand{position:absolute;left:40px;top:62px;display:flex;align-items:center;gap:10px}
  .brand-dot{width:14px;height:14px;background:var(--yellow)}
  .brand-name{font-weight:800;font-size:22px;letter-spacing:.2px;color:var(--ink);white-space:nowrap}

  .portrait{position:absolute;left:0;top:112px;width:483px;height:443px;background:linear-gradient(180deg,var(--photo-a) 0%,var(--photo-b) 70%,var(--photo-c) 100%)}
  .photo-band{position:absolute;left:0;top:555px;width:483px;height:11px;background:var(--yellow)}

  .headline{position:absolute;left:36px;top:586px;font-weight:400;font-size:60px;line-height:68px;color:var(--ink);letter-spacing:-.5px}
  .headline-accent{position:absolute;left:34px;top:722px;font-weight:800;font-size:80px;line-height:86px;color:var(--yellow);letter-spacing:-1px}
  .headline-rule{position:absolute;left:36px;top:824px;width:140px;height:4px;background:var(--ink)}
  .website{position:absolute;left:36px;top:842px;font-size:26px;font-weight:500;color:var(--ink)}

  .intro{position:absolute;left:520px;top:44px;width:630px;text-align:center;font-style:italic;font-weight:600;font-size:20px;line-height:26px;color:var(--ink)}
  .intro-rule{position:absolute;left:779px;top:160px;width:140px;height:4px;background:var(--ink)}

  .section-title{position:absolute;left:518px;top:188px;font-weight:800;font-size:36px;color:var(--white);letter-spacing:.5px}

  .service{position:absolute;left:542px;width:620px}
  .service-icon{position:absolute;left:0;top:0;width:58px;height:58px}
  .service-body{position:absolute;left:85px;top:0;width:500px}
  .service-name{font-weight:700;font-size:14.5px;line-height:18px;color:var(--ink)}
  .service-text{font-size:10.4px;line-height:12.4px;text-transform:uppercase;color:var(--ink);margin-top:2px}
  .benefits{margin:10px 0 0 42px}
  .benefits-title{font-style:italic;font-weight:700;font-size:13px;margin-bottom:4px}
  .benefits ul{list-style:none;margin-left:14px}
  .benefits li{position:relative;font-size:10px;line-height:12px;padding-left:18px;margin-bottom:3px;width:420px}
  .benefits li svg{position:absolute;left:0;top:1px}

  .contact-title{position:absolute;left:518px;top:784px;font-weight:800;font-size:33px;color:var(--white)}
  .contact-tag{position:absolute;left:520px;top:822px;font-style:italic;font-weight:600;font-size:18px;line-height:26px;color:var(--ink)}
  .contact-divider{position:absolute;left:786px;top:786px;width:3px;height:92px;background:var(--ink)}
  .contact-list{position:absolute;left:812px;top:785px}
  .contact-row{position:relative;padding-left:32px;color:var(--ink)}
  .contact-row svg{position:absolute;left:0}
  .contact-name{font-weight:700;font-size:14px;line-height:16px}
  .contact-role{font-size:14px;line-height:17px}
  .contact-phone{font-weight:800;font-size:26px;margin-top:6px;line-height:30px}
  .contact-mail{font-weight:600;font-size:13px;margin-top:8px}
</style>
</head>
<body>
<main class="flyer">
  <section class="side-panel">
    <div class="brand">
      <div class="brand-dot"></div>
      <div class="brand-name">HOLLIS VARGA CONSULTING</div>
    </div>
  </section>

  <div class="portrait" role="img" aria-label="Portrait photograph of the consultant, smiling, in a blue top"></div>
  <div class="photo-band"></div>

  <div class="headline">Helping you<br>navigate</div>
  <div class="headline-accent">BSAQP.</div>
  <div class="headline-rule"></div>
  <div class="website">hollisvargaconsulting.com</div>

  <section class="main-panel"></section>

  <p class="intro">15 Years Of Metabolic &amp; Bariatric Surgery<br>Field Experience. Developing quality improvement<br>processes that will track performance improvement,<br>safety, and patient outcomes.</p>
  <div class="intro-rule"></div>

  <h2 class="section-title">WE PROVIDE</h2>

  <article class="service" style="top:248px">
    <svg class="service-icon" viewBox="0 0 58 58"><circle cx="29" cy="29" r="29" fill="#1d1d1b"/><rect x="13" y="30" width="32" height="10" fill="#f7d417"/><circle cx="23" cy="21" r="4" fill="#f7d417"/><circle cx="35" cy="21" r="4" fill="#f7d417"/></svg>
    <div class="service-body">
      <h3 class="service-name">MBSCR STAFFING</h3>
      <p class="service-text">Maintain compliance with BSAQP data abstraction with a data abstractor who will be a member of your team, provide leadership and direction in the development of QI projects, perform routine quality assurance audits on data and attend all bariatric team meetings.</p>
      <div class="benefits">
        <p class="benefits-title">Why we need MBSCR?</p>
        <ul>
          <li><svg width="12" height="10" viewBox="0 0 12 10"><path d="M1 5l3.5 3.5L11 1" stroke="#1d1d1b" stroke-width="2" fill="none"/></svg>It’s Cost Effective as facility pays no employee benefits, freeing up valuable resources for other program needs</li>
          <li><svg width="12" height="10" viewBox="0 0 12 10"><path d="M1 5l3.5 3.5L11 1" stroke="#1d1d1b" stroke-width="2" fill="none"/></svg>Experienced nurses provide leadership and direction in development of QI/PI process</li>
          <li><svg width="12" height="10" viewBox="0 0 12 10"><path d="M1 5l3.5 3.5L11 1" stroke="#1d1d1b" stroke-width="2" fill="none"/></svg>Looks for opportunities to facilitate quality improvement in your program</li>
        </ul>
      </div>
    </div>
  </article>

  <article class="service" style="top:440px">
    <svg class="service-icon" viewBox="0 0 58 58"><circle cx="29" cy="29" r="29" fill="#1d1d1b"/><rect x="19" y="15" width="18" height="26" fill="none" stroke="#f7d417" stroke-width="2"/><path d="M23 22h10M23 27h10M23 32h6" stroke="#f7d417" stroke-width="2"/><path d="M32 40l9-12" stroke="#f7d417" stroke-width="3"/></svg>
    <div class="service-body">
      <h3 class="service-name">PROGRAM ASSESSMENT</h3>
      <p class="service-text">A 2-day on-site assessment of your bariatric program as it relates to BSAQP compliance, best practice, business strategies and evaluation of the process for collecting outcomes data. A comprehensive post-assessment review and written report will provide guidance, solutions, timelines and suggest opportunities for improvement.</p>
    </div>
  </article>

  <article class="service" style="top:551px">
    <svg class="service-icon" viewBox="0 0 58 58"><circle cx="29" cy="29" r="29" fill="#1d1d1b"/><rect x="17" y="20" width="24" height="22" fill="none" stroke="#f7d417" stroke-width="2"/><path d="M22 26h4M32 26h4M22 32h4M32 32h4M27 42v-6h4v6" stroke="#f7d417" stroke-width="2" fill="none"/><path d="M29 12v6M26 15h6" stroke="#f7d417" stroke-width="2"/></svg>
    <div class="service-body">
      <h3 class="service-name">PROGRAM DEVELOPMENT— REMOTE ASSISTANCE &amp; ON-SITE</h3>
      <p class="service-text">For centers currently developing a new program, assistance by experienced professionals can help to ensure accreditation and provide guidance in the development of policies and procedures, job descriptions, clinical pathways and protocols that will enhance program as well as ensure BSAQP compliance. With the remote option consultant will meet with staff during regularly scheduled webinars.</p>
    </div>
  </article>

  <article class="service" style="top:680px">
    <svg class="service-icon" viewBox="0 0 58 58"><circle cx="29" cy="29" r="29" fill="#1d1d1b"/><circle cx="22" cy="19" r="4" fill="#f7d417"/><path d="M16 44V28h12v16" fill="#f7d417"/><rect x="31" y="24" width="11" height="14" fill="none" stroke="#f7d417" stroke-width="2"/><path d="M33 31l3 3 5-6" stroke="#f7d417" stroke-width="2" fill="none"/></svg>
    <div class="service-body">
      <h3 class="service-name">MOCK SITE INSPECTIONS</h3>
      <p class="service-text">This one-day rigorous evaluation of a facility evaluates accreditation readiness by providing a critical assessment of all areas related to the standards for BSAQP accreditation. It closely mirrors the BSAQP site survey process.</p>
    </div>
  </article>

  <h2 class="contact-title">CONTACT US</h2>
  <p class="contact-tag">Start improving your<br>bariatric program today</p>
  <div class="contact-divider"></div>
  <div class="contact-list">
    <div class="contact-row">
      <svg width="16" height="18" viewBox="0 0 16 18" style="top:1px"><circle cx="8" cy="5" r="4.5" fill="#1d1d1b"/><path d="M0 18c0-5 3.5-7.5 8-7.5S16 13 16 18z" fill="#1d1d1b"/></svg>
      <div class="contact-name">Hollis Varga, RN, CBN</div>
      <div class="contact-role">Bariatric Program Consultant</div>
    </div>
    <div class="contact-row contact-phone">
      <svg width="20" height="22" viewBox="0 0 20 22" style="top:4px"><path d="M4 1l4 5-2.5 2.5c1.5 3 4 5.5 7 7L15 13l5 4-3 4C9 20 1 12 0 4z" fill="#1d1d1b"/></svg>
      555-014-2280
    </div>
    <div class="contact-row contact-mail">
      <svg width="18" height="13" viewBox="0 0 18 13" style="top:2px"><rect x="0.5" y="0.5" width="17" height="12" fill="#1d1d1b"/><path d="M1 1l8 6 8-6" stroke="#f7d417" stroke-width="1.5" fill="none"/></svg>
      hollis@hollisvargaconsulting.com
    </div>
  </div>
</main>
</body>
</html>
```